Tech Company Letterhead/Business Cards/Envelopes

We would like a new stationary design for a technology company that develops full turnkey solutions for governments related to Data, Identity Tracking, Fingerprinting, Passport Control, and Border Protection Systems.

We would like the stationary designs to include:

Letter Head
Business Cards
Envelopes

Target Market(s)

Corporate

Industry/Entity Type

Business

Contact Information for Business Card

Details to be shared with the winner.

Font styles to use
Serif
Sans Serif

Colors
e4daeb
85abd2
3176b5
0355a3
0692cd

```html
<!DOCTYPE html>
<html lang="en">
<head>
<meta charset="utf-8">
<title>Orvake Stationery</title>
<link href="https://fonts.googleapis.com/css2?family=Exo+2:wght@400;600;700&family=Roboto:wght@400&display=swap" rel="stylesheet">
<style>
  :root{
    --stage:#3a3a3c;
    --paper:#ffffff;
    --ink:#6b6b6b;
    --brand:#0a6fbf;
    --brand-deep:#0355a3;
    --mid:#85abd2;
    --cyan:#0692cd;
    --cyan-bright:#1fc2ef;
    --mist:#dfe9e6;
    --label:#ffffff;
    --corner-fade:linear-gradient(135deg,#e4ecef 0%,#85abd2 45%,#1fb8ea 100%);
  }
  *{margin:0;padding:0;box-sizing:border-box}
  html,body{width:1200px;height:793px;overflow:hidden;background:var(--stage)}
  body{position:relative;font-family:"Exo 2",sans-serif;color:var(--ink)}
  .sheet{position:absolute;background:var(--paper);overflow:hidden;box-shadow:2px 3px 6px rgba(0,0,0,.45)}
  .corner-art{position:absolute;right:0;bottom:0;background:var(--corner-fade);clip-path:polygon(100% 0,100% 100%,0 100%)}
  .wordmark{position:absolute;font-family:"Exo 2",sans-serif;font-weight:700;color:var(--brand);letter-spacing:.05em;line-height:1;white-space:nowrap}
  .info{position:absolute;font-size:6.4px;line-height:1.55;color:var(--ink);white-space:nowrap}
  .info .name{color:var(--brand);font-weight:600;letter-spacing:.04em}
  .info .key{color:var(--brand);font-weight:600}
  .info .web{color:var(--brand);font-weight:600;letter-spacing:.05em}
  .divider{position:absolute;width:1px;background:#9a9a9a}
  .url-spaced{position:absolute;font-size:8px;letter-spacing:.32em;color:var(--ink);white-space:nowrap}
  .option-label{position:absolute;font-family:"Roboto",sans-serif;font-size:16px;color:var(--label);transform:translateX(-50%);white-space:nowrap}

  .letterhead{left:62px;top:102px;width:489px;height:633px}
  .letterhead .wordmark{left:25px;top:38px;font-size:34px}
  .letterhead .corner-art{width:170px;height:230px}

  .card{width:251px;height:143px}
  .card-front-1{left:604px;top:66px}
  .card-front-1 .wordmark{left:15px;top:18px;font-size:31px}
  .card-front-1 .corner-art{width:62px;height:80px}
  .card-front-2{left:603px;top:224px;height:144px}
  .card-front-2 .wordmark{left:16px;top:15px;font-size:31px}
  .card-front-2 .corner-art{width:130px;height:135px}
  .card-back-1{left:867px;top:66px}
  .card-back-1 .wordmark{left:13px;top:14px;font-size:21px}
  .card-back-1 .corner-art{width:230px;height:143px}
  .card-back-2{left:866px;top:224px}
  .card-back-2 .deep-field{position:absolute;inset:0;background:linear-gradient(150deg,#0355a3 0%,#0a7fd0 55%,#1fc2ef 100%)}
  .card-back-2 .white-corner{position:absolute;right:0;bottom:0;width:120px;height:75px;background:var(--paper);clip-path:polygon(100% 0,100% 100%,0 100%)}
  .card-back-2 .url-spaced{left:12px;top:10px;color:#d8e8f6}
  .card-back-2 .wordmark{left:156px;top:119px;font-size:17px}

  .flap{position:absolute;left:594px;top:422px;width:558px;height:64px}
  .flap svg{display:block;width:100%;height:100%;filter:drop-shadow(1px 3px 3px rgba(0,0,0,.45))}

  .envelope{left:590px;top:501px;width:560px;height:252px}
  .envelope .wordmark{left:28px;top:195px;font-size:39px}
  .envelope .corner-art{width:180px;height:150px}
</style>
</head>
<body>

<!-- Letterhead -->
<section class="sheet letterhead">
  <div class="wordmark">ORVAKE</div>
  <div class="info" style="left:25px;top:596px;">
    <div class="name">ORVAKE COMPANY NAME</div>
    <div>PO Box 01234, City Name,</div>
    <div>Country Name 00000</div>
  </div>
  <div class="divider" style="left:122px;top:598px;height:28px;"></div>
  <div class="info" style="left:128px;top:596px;">
    <div><span class="key">Phone :</span> 012 345 6789</div>
    <div><span class="key">Email :</span> info@orvake.com</div>
    <div class="web" style="font-size:7.4px">www.orvake.com</div>
  </div>
  <div class="corner-art" role="img" aria-label="Diagonal blue corner graphic"></div>
</section>

<!-- Business cards -->
<div class="option-label" style="left:743px;top:44px;">Front option 1</div>
<section class="sheet card card-front-1">
  <div class="wordmark">ORVAKE</div>
  <div class="info" style="left:15px;top:105px;">
    <div class="name">ORVAKE COMPANY NAME</div>
    <div>PO Box 01234, City Name,</div>
    <div>Country Name 00000</div>
  </div>
  <div class="divider" style="left:110px;top:108px;height:24px;"></div>
  <div class="info" style="left:124px;top:104px;">
    <div><span class="key">Phone</span> &nbsp;: 012 345 6789</div>
    <div><span class="key">Email</span> &nbsp;&nbsp;: info@orvake.com</div>
    <div class="web">www.orvake.com</div>
  </div>
  <div class="corner-art" role="img" aria-label="Diagonal blue corner graphic"></div>
</section>

<div class="option-label" style="left:1000px;top:44px;">Back option 1</div>
<section class="sheet card card-back-1">
  <div class="corner-art" role="img" aria-label="Diagonal blue corner graphic"></div>
  <div class="wordmark">ORVAKE</div>
  <div class="url-spaced" style="left:14px;top:39px;">www.orvake.com</div>
</section>

<section class="sheet card card-front-2">
  <div class="wordmark">ORVAKE</div>
  <div class="info" style="left:16px;top:68px;">
    <div class="name">ORVAKE COMPANY NAME</div>
    <div>PO Box 01234, City Name,</div>
    <div>Country Name 00000</div>
  </div>
  <div class="info" style="left:16px;top:104px;">
    <div><span class="key">Phone</span> &nbsp;&nbsp;: 012 345 6789</div>
    <div><span class="key">Email</span> &nbsp;&nbsp;&nbsp;: info@orvake.com</div>
    <div class="web" style="margin-top:2px">www.orvake.com</div>
  </div>
  <div class="corner-art" role="img" aria-label="Diagonal blue corner graphic"></div>
</section>
<div class="option-label" style="left:737px;top:373px;">Front option 2</div>

<section class="sheet card card-back-2">
  <div class="deep-field" role="img" aria-label="Deep blue diagonal background graphic"></div>
  <div class="white-corner"></div>
  <div class="url-spaced">www.orvake.com</div>
  <div class="wordmark">ORVAKE</div>
</section>
<div class="option-label" style="left:993px;top:369px;">Back option 2</div>

<!-- Envelope -->
<div class="flap">
  <svg viewBox="0 0 558 64" preserveAspectRatio="none" role="img" aria-label="Envelope flap with blue gradient edge">
    <defs>
      <linearGradient id="flapFade" x1="0" y1="0" x2="1" y2="0">
        <stop offset="0" stop-color="#e4ecef"/>
        <stop offset=".5" stop-color="#85abd2"/>
        <stop offset="1" stop-color="#1fb8ea"/>
      </linearGradient>
      <clipPath id="flapClip"><path d="M0,0 H558 L540,40 Q530,63 500,64 H60 Q35,64 25,45 Z"/></clipPath>
    </defs>
    <path d="M0,0 H558 L540,40 Q530,63 500,64 H60 Q35,64 25,45 Z" fill="var(--paper)"/>
    <polygon clip-path="url(#flapClip)" points="30,64 558,14 558,64" fill="url(#flapFade)"/>
  </svg>
</div>

<section class="sheet envelope">
  <div class="wordmark">ORVAKE</div>
  <div class="divider" style="left:228px;top:198px;height:30px;"></div>
  <div class="info" style="left:234px;top:198px;line-height:1.85;">
    <div>PO Box 01234, City Name, Country Name 00000</div>
    <div><span class="key">Phone :</span> 012 345 6789 &nbsp;&nbsp;<span class="key">Email:</span> info@orvake.com</div>
    <div class="web">www.orvake.com</div>
  </div>
  <div class="corner-art" role="img" aria-label="Diagonal blue corner graphic"></div>
</section>
</body>
</html>
```